Business Card for: Northbrook Financial Advisory Services Inc.

provide strategic financial advisory services to companies in the areas of corporate finance, mergers and acquisitions, executive coaching and strategic planning

Target Market(s)

Companies, banks, accountants, lawyers

Industry/Entity Type

High end business consulting in corporate finance, mergers and acquisitions, consulting

Contact Information for Business Card

Name of company, Name: xxxxxx xxxxxx , CEO, - phone number: 1-xxx-xxx-xxxx, - email address,

Requirements
Must have
• Must be professional and simple.
Nice to have
• simple, straight graphics, must give the impression that we are trustworthy, professional, competent
Should not have
• loud colors, loud design features

```html
<!DOCTYPE html>
<html lang="en">
<head>
<meta charset="utf-8">
<title>Northbrook Financial Advisory Services Inc. – Business Card</title>
<link rel="stylesheet" href="https://fonts.googleapis.com/css2?family=Orbitron:wght@700&family=Arimo:wght@400;500&display=swap">
<style>
  :root {
    --backdrop: #2b2b2b;
    --card: #161616;
    --gold: #f2a81d;
    --white: #ffffff;
    --muted: #e6e6e6;
    --shadow: rgba(0, 0, 0, 0.45);
  }
  * { margin: 0; padding: 0; box-sizing: border-box; }
  html, body {
    width: 1200px;
    height: 800px;
    overflow: hidden;
    background: var(--backdrop);
  }
  .canvas {
    position: relative;
    width: 1200px;
    height: 800px;
    display: flex;
    align-items: center;
    justify-content: center;
    gap: 60px;
  }
  .card {
    position: relative;
    width: 525px;
    height: 300px;
    background: var(--card);
    border-radius: 14px;
    box-shadow: 0 10px 0 #0d0d0d, 0 24px 40px var(--shadow);
    overflow: hidden;
  }

  /* Front */
  .wordmark {
    position: absolute;
    left: 58px;
    top: 108px;
    font-family: "Orbitron", sans-serif;
    font-weight: 700;
    color: var(--gold);
    text-transform: uppercase;
    line-height: 1.1;
  }
  .wordmark-line {
    display: block;
    font-size: 27px;
    letter-spacing: 0.5px;
  }
  .wordmark-row {
    display: flex;
    align-items: flex-end;
    gap: 14px;
  }
  .wordmark-sub {
    position: relative;
    font-size: 11px;
    letter-spacing: 3.5px;
    padding-bottom: 4px;
    white-space: nowrap;
  }
  .wordmark-sub::after {
    content: "";
    position: absolute;
    left: 40px;
    top: 24px;
    width: 120px;
    height: 1px;
    background: var(--muted);
  }

  /* Back */
  .person {
    position: absolute;
    left: 0;
    right: 0;
    top: 78px;
    text-align: center;
    padding-left: 40px;
  }
  .person-name {
    font-family: "Orbitron", sans-serif;
    font-weight: 700;
    color: var(--gold);
    font-size: 20px;
    letter-spacing: 1px;
  }
  .person-title {
    font-family: "Orbitron", sans-serif;
    font-weight: 700;
    color: var(--white);
    font-size: 11px;
    letter-spacing: 2px;
    margin-top: 8px;
  }
  .person-rule {
    width: 50px;
    height: 1px;
    background: var(--muted);
    margin: 10px auto 0;
  }
  .contacts {
    position: absolute;
    left: 30px;
    right: 20px;
    top: 192px;
    display: flex;
    justify-content: space-between;
    list-style: none;
    font-family: "Arimo", sans-serif;
    font-size: 13.5px;
    color: var(--white);
  }
  .contact-item {
    display: flex;
    align-items: center;
    gap: 6px;
  }
  .contact-icon { width: 11px; height: 11px; flex: none; }
  .stripes {
    position: absolute;
    left: 0;
    bottom: 38px;
    width: 525px;
    height: 8px;
  }
</style>
</head>
<body>
<main class="canvas">

  <section class="card card-front" aria-label="Card front">
    <h1 class="wordmark">
      <span class="wordmark-line">Northbrook</span>
      <span class="wordmark-row">
        <span class="wordmark-line">Financial</span>
        <span class="wordmark-sub">Advisory Inc.</span>
      </span>
    </h1>
  </section>

  <section class="card card-back" aria-label="Card back">
    <div class="person">
      <h2 class="person-name">DANIEL WHITAKER</h2>
      <p class="person-title">CEO</p>
      <div class="person-rule"></div>
    </div>

    <ul class="contacts">
      <li class="contact-item">
        <svg class="contact-icon" viewBox="0 0 12 12" aria-hidden="true">
          <rect x="2.5" y="0.5" width="7" height="11" rx="1.2" fill="none" stroke="#f2a81d" stroke-width="1.2"/>
          <line x1="5" y1="9.5" x2="7" y2="9.5" stroke="#f2a81d" stroke-width="1"/>
        </svg>
        044-555 210 347
      </li>
      <li class="contact-item">
        <svg class="contact-icon" viewBox="0 0 12 12" aria-hidden="true">
          <path d="M1 6 L11 1 L7 11 L6 7 Z" fill="#f2a81d"/>
        </svg>
        info@northbrookfa.com
      </li>
      <li class="contact-item">
        <svg class="contact-icon" viewBox="0 0 12 12" aria-hidden="true">
          <circle cx="6" cy="6" r="5.5" fill="#f2a81d"/>
          <path d="M0.5 6 H11.5 M6 0.5 C3 3 3 9 6 11.5 M6 0.5 C9 3 9 9 6 11.5" fill="none" stroke="#161616" stroke-width="0.9"/>
        </svg>
        www.northbrookfa.com
      </li>
    </ul>

    <svg class="stripes" viewBox="0 0 525 8" preserveAspectRatio="none" aria-hidden="true">
      <polygon points="0,2 318,2 314,8 0,8" fill="#f2a81d"/>
      <polygon points="326,0 525,0 525,8 320,8" fill="#ffffff"/>
    </svg>
  </section>

</main>
</body>
</html>
```